Corporate Dinner Invite at Verolla for PMV

PMV is hosting a corporate dinner at the BRQ Conference and we need an email attachment invite for the event. Please use some images from this site for inspiration: https://www.verollaexample.com/fernparlor/

Invite Title:
Join us for dinner!

Event Details:
Tuesday, October 24th 2023 at 6:30pm
Verolla Chicago, Fern Parlor
347 W Harlow Ave, Chicago, IL 60622

Target Market(s)

Corporate Audience

Font styles to use
Script

Colors
0054AA
0677BA
7BADD7
CADEEF
E8F1F8

Requirements
Must have
• PMV logo, event date / time, event location details, photo(s) from Fern Parlor

```html
<!DOCTYPE html>
<html lang="en">
<head>
<meta charset="utf-8">
<title>PMV Dinner Invitation</title>
<link href="https://fonts.googleapis.com/css2?family=Great+Vibes&family=Alegreya:wght@400;700&display=swap" rel="stylesheet">
<style>
  :root {
    --page-bg: #dfe0e3;
    --card-bg: #ffffff;
    --navy: #0b2d8c;
    --frame-blue: #0677ba;
    --brand-blue: #0054aa;
    --gold: #cdb48e;
    --photo-dark: #2a1a10;
    --photo-warm: #8a5a2a;
  }
  * { margin: 0; padding: 0; box-sizing: border-box; }
  html, body { width: 1200px; height: 1200px; overflow: hidden; }
  body { background: var(--page-bg); position: relative; font-family: "Alegreya", Georgia, serif; }

  .invite-card {
    position: absolute; left: 205px; top: 47px; width: 790px; height: 1105px;
    background: var(--card-bg); border: 9px solid var(--navy);
    box-shadow: 0 4px 14px rgba(0,0,0,0.18);
  }
  .host-brand {
    position: absolute; left: 0; right: 0; top: 112px;
    display: flex; justify-content: center; align-items: center; gap: 14px;
  }
  .host-brand .brand-square { width: 44px; height: 44px; background: var(--brand-blue); }
  .host-brand .brand-name {
    font-weight: 700; font-size: 58px; color: var(--brand-blue); letter-spacing: 2px; line-height: 1;
  }
  .photo-frame {
    position: absolute; left: 248px; top: 245px; width: 702px; height: 409px;
    border: 2px solid var(--frame-blue); border-radius: 12px; background: var(--card-bg);
  }
  .photo-frame .venue-photo {
    position: absolute; left: 18px; top: 15px; width: 666px; height: 375px; border-radius: 14px;
    background: linear-gradient(180deg, var(--photo-dark) 0%, #4a2c16 45%, var(--photo-warm) 70%, #d9d4cc 100%);
  }
  .invite-title {
    position: absolute; left: 0; width: 1200px; top: 655px; text-align: center;
    font-family: "Great Vibes", cursive; font-size: 104px; color: var(--navy); line-height: 1.2;
  }
  .event-date {
    position: absolute; left: 0; width: 1200px; top: 805px; text-align: center;
    font-weight: 700; font-size: 34px; color: var(--navy);
  }
  .venue-mark {
    position: absolute; left: 549px; top: 866px; width: 96px; height: 96px;
    border: 2px solid var(--gold); border-radius: 50%;
  }
  .venue-name {
    position: absolute; left: 0; width: 1200px; top: 985px; text-align: center;
    font-weight: 400; font-size: 42px; color: var(--gold); letter-spacing: 4px; line-height: 1;
  }
  .venue-address {
    position: absolute; left: 0; width: 1200px; top: 1043px; text-align: center;
    font-weight: 700; font-size: 27px; color: var(--navy); line-height: 40px;
  }
</style>
</head>
<body>
  <div class="invite-card"></div>

  <div class="host-brand">
    <span class="brand-square"></span>
    <span class="brand-name">PMV</span>
  </div>

  <div class="photo-frame">
    <div class="venue-photo" role="img" aria-label="Row of crafted cocktails on a marble bar in front of softly lit shelves of bottles at Fern Parlor"></div>
  </div>

  <h1 class="invite-title">Join us for dinner!</h1>
  <p class="event-date">Tuesday, October 24th 2023 at 6:30pm</p>

  <div class="venue-mark"></div>
  <p class="venue-name">VEROLLA</p>

  <p class="venue-address">Verolla Chicago, Fern Parlor<br>347 W Harlow Ave, Chicago, IL 60622</p>
</body>
</html>
```